Tallow Farm Brochure

To design a small brochure that tells people about our U-Pick cherry farm, where we are, when we are open and what our contact details are.

We have existing logo's which should be used. I have uploaded a file with these details.

Details about us are all located on:-
www.friendlink.example/tallowfarm
https://circlepage.example/u/0/b/704916382057419263851/704916382057419263851/about/p/pub

Farm

```html
<!DOCTYPE html>
<html lang="en">
<head>
<meta charset="utf-8">
<title>Tallow Farm Brochure</title>
<link href="https://fonts.googleapis.com/css2?family=Lato:wght@300;400;700&display=swap" rel="stylesheet">
<style>
  :root {
    --stage: #cfd0d1;
    --paper: #ffffff;
    --brand-green: #3d9a48;
    --lime: #9ccc3c;
    --lime-light: #c9dc4e;
    --teal: #2f8a73;
    --cherry: #8a2b22;
    --purple: #8a4aa8;
    --sun: #f7dc6a;
    --sky: #bfe2f2;
    --ink: #5d5d5d;
    --ink-soft: #8a8a8a;
  }
  * { box-sizing: border-box; margin: 0; padding: 0; }
  html, body { width: 1200px; height: 795px; overflow: hidden; }
  body { background: var(--stage); font-family: "Lato", Arial, sans-serif; position: relative; }

  .brochure {
    position: absolute; left: 330px; top: 28px;
    width: 540px; height: 740px;
    background: var(--paper);
    box-shadow: 0 6px 18px rgba(0,0,0,.18);
    overflow: hidden;
  }
  .hero-art { position: absolute; left: 0; top: 0; width: 540px; height: 500px; }

  .brand-name {
    position: absolute; font-family: "Lato", Arial, sans-serif; font-weight: 700;
    color: var(--brand-green); display: flex; align-items: center; gap: 6px; white-space: nowrap;
  }
  .brand-dot { width: 10px; height: 10px; border-radius: 50%; background: var(--lime); }
  .brand-name--top { left: 36px; top: 34px; font-size: 26px; }
  .brand-name--footer { left: 196px; top: 690px; font-size: 24px; }

  .section-bar {
    position: absolute; top: 500px; height: 30px;
    background: linear-gradient(90deg, var(--lime), var(--lime-light));
    color: #fff; font-size: 16px; font-weight: 400; line-height: 30px;
  }
  .section-bar--who { left: 0; width: 200px; padding-left: 26px; }
  .section-bar--value { left: 340px; width: 167px; padding-left: 60px; border-radius: 0 15px 15px 0; }

  .timings {
    position: absolute; left: 179px; top: 476px; width: 187px; height: 190px;
    border-radius: 34px;
    background: linear-gradient(180deg, var(--lime) 0%, #55a85a 55%, var(--teal) 100%);
    color: #fff;
  }
  .timings-title {
    margin: 17px auto 0; width: 140px; height: 32px; border: 1.5px solid rgba(255,255,255,.85);
    border-radius: 16px; text-align: center; font-size: 17px; font-weight: 300; line-height: 29px;
  }
  .timings-list { list-style: none; margin: 24px 0 0 18px; }
  .timings-list li { display: flex; align-items: center; height: 32px; font-size: 10px; font-weight: 300; }
  .timings-list b { font-weight: 700; margin: 0 6px 0 8px; }
  .chevrons { width: 16px; height: 12px; }

  .column-copy {
    position: absolute; top: 542px; font-size: 6.4px; line-height: 8.4px;
    color: var(--ink); text-align: justify;
  }
  .column-copy p + p { margin-top: 3px; }
  .column-copy--who { left: 40px; width: 128px; }
  .column-copy--value { left: 376px; width: 124px; }

  .web-links {
    position: absolute; left: 40px; top: 688px; font-size: 9px; line-height: 15px; color: var(--ink-soft);
  }
  .call-us { position: absolute; left: 372px; top: 676px; color: var(--ink-soft); }
  .call-us-label { font-size: 11px; margin-left: 46px; line-height: 13px; }
  .call-us-number { font-size: 23px; font-weight: 400; color: var(--ink); letter-spacing: .5px; line-height: 28px; }
</style>
</head>
<body>
<main class="brochure">
  <svg class="hero-art" viewBox="0 0 540 500" xmlns="http://www.w3.org/2000/svg">
    <defs>
      <radialGradient id="whiteDisc" cx="50%" cy="45%" r="55%">
        <stop offset="0%" stop-color="#ffffff"/>
        <stop offset="80%" stop-color="#f4f4f4"/>
        <stop offset="100%" stop-color="#dedede"/>
      </radialGradient>
      <linearGradient id="greenDisc" x1="0" y1="0" x2="0" y2="1">
        <stop offset="0%" stop-color="#8cc540"/>
        <stop offset="100%" stop-color="#2f8a73"/>
      </linearGradient>
      <linearGradient id="orchardTone" x1="0" y1="0" x2="1" y2="1">
        <stop offset="0%" stop-color="#6f9a3c"/>
        <stop offset="100%" stop-color="#2f5a25"/>
      </linearGradient>
      <linearGradient id="vanTone" x1="0" y1="0" x2="1" y2="0">
        <stop offset="0%" stop-color="#f1f3f1"/>
        <stop offset="60%" stop-color="#e7efe2"/>
        <stop offset="100%" stop-color="#b9d98a"/>
      </linearGradient>
    </defs>

    <circle class="ring" cx="208" cy="222" r="136" fill="none" stroke="#e3e6ea" stroke-width="1.2"/>
    <circle class="ring" cx="505" cy="108" r="9" fill="none" stroke="#cfe3ee" stroke-width="1"/>
    <circle class="ring" cx="465" cy="118" r="6" fill="none" stroke="#cfe3ee" stroke-width="1"/>

    <circle cx="292" cy="90" r="74" fill="var(--lime-light)" opacity=".85"/>
    <circle cx="370" cy="208" r="108" fill="var(--cherry)"/>
    <circle cx="215" cy="380" r="56" fill="var(--purple)"/>
    <circle cx="104" cy="339" r="22" fill="var(--purple)"/>
    <circle cx="420" cy="352" r="28" fill="var(--sun)" opacity=".85"/>
    <circle cx="270" cy="437" r="28" fill="var(--sun)" opacity=".8"/>
    <circle cx="193" cy="70" r="15" fill="var(--sun)" opacity=".85"/>
    <circle cx="393" cy="70" r="22" fill="var(--sky)"/>
    <circle cx="425" cy="260" r="20" fill="var(--lime-light)"/>
    <circle cx="128" cy="290" r="7" fill="#e9b4c8"/>
    <circle cx="120" cy="393" r="5" fill="var(--lime-light)"/>
    <circle cx="465" cy="245" r="4" fill="var(--sun)"/>
    <circle cx="474" cy="385" r="4" fill="#f08060"/>
    <circle cx="358" cy="108" r="3" fill="#f08060"/>

    <circle cx="208" cy="220" r="113" fill="url(#whiteDisc)"/>
    <rect x="108" y="180" width="206" height="84" rx="8" fill="url(#vanTone)" role="img" aria-label="Photo of the farm's white delivery van with green branding"/>

    <circle cx="413" cy="146" r="62" fill="url(#orchardTone)" stroke="#fff" stroke-width="3" role="img" aria-label="Photo of a farmer among leafy cherry trees"/>
    <circle cx="196" cy="392" r="62" fill="url(#orchardTone)" stroke="#fff" stroke-width="3" role="img" aria-label="Photo of a picker in the cherry orchard"/>

    <circle cx="355" cy="326" r="96" fill="url(#greenDisc)"/>
    <g class="headline" fill="#fff" text-anchor="middle" font-family="Lato, Arial, sans-serif">
      <text x="355" y="294" font-size="20" font-weight="300" letter-spacing=".5">HAPPY TREES</text>
      <text x="355" y="311" font-size="10.5" font-weight="400" letter-spacing=".4">THAT'S WHAT MAKES OUR</text>
      <text x="355" y="343" font-size="30" font-weight="700">CHERRIES</text>
      <text x="355" y="361" font-size="10.5" font-weight="400" letter-spacing=".6">JUICIER AND SWEETER</text>
    </g>
  </svg>

  <div class="brand-name brand-name--top"><span class="brand-dot"></span>Tallow Farm</div>

  <div class="section-bar section-bar--who">Who We Are?</div>
  <div class="section-bar section-bar--value">We Value!</div>

  <section class="timings">
    <h2 class="timings-title">Our Timings</h2>
    <ul class="timings-list">
      <li><svg class="chevrons" viewBox="0 0 16 12"><path d="M1 1l5 5-5 5M8 1l5 5-5 5" fill="none" stroke="#fff" stroke-width="2"/></svg><b>Sunday</b>10:00 am – 5:00 pm</li>
      <li><svg class="chevrons" viewBox="0 0 16 12"><path d="M1 1l5 5-5 5M8 1l5 5-5 5" fill="none" stroke="#fff" stroke-width="2"/></svg><b>Friday</b>10:00 am – 5:00 pm</li>
      <li><svg class="chevrons" viewBox="0 0 16 12"><path d="M1 1l5 5-5 5M8 1l5 5-5 5" fill="none" stroke="#fff" stroke-width="2"/></svg><b>Saturday</b>10:00 am – 5:00 pm</li>
    </ul>
  </section>

  <div class="column-copy column-copy--who">
    <p>Nestled in a quiet green valley, an ideal spot to grow sweet and juicy cherries. Visit us for a day of picking fresh cherries straight from the tree.</p>
    <p>Bring a bucket and pick as much as you want. Prices are kept fair and listed per kilo. There are no entry fees for children.</p>
    <p>We open our gates during the season so the whole family can wander among the trees and taste the fruit. Come and see how our cherries are grown and the care we give to managing our trees.</p>
  </div>

  <div class="column-copy column-copy--value">
    <p>We have twelve varieties of cherries, most of which are heritage varieties rarely found elsewhere. Some have dark, near black fruit and others have red blush fruit. Our cherries are mid-season and are typically available in November and December.</p>
    <p>Tallow Farm was previously run by two generations of one local family.</p>
    <p>Farmer Ned is a third generation farmer who moved to the valley and now welcomes pickers each season.</p>
  </div>

  <div class="web-links">
    <div>www.tallowfarm.example</div>
    <div>mail@tallowfarm.example</div>
  </div>

  <div class="brand-name brand-name--footer"><span class="brand-dot"></span>Tallow Farm</div>

  <div class="call-us">
    <div class="call-us-label">Call Us For More Info!</div>
    <div class="call-us-number">1300 555 018</div>
  </div>
</main>
</body>
</html>
```